Flyer Advertisement Simple But Creative

Flyer dimensions 4" x 6"

Simple design with logo and additional info. On the front of the flyer:

- place the logo at the top
- beneath the logo add the website and phone number
- simple less is more approach
- feel free to add your own personal touch

On the back:

- Requirements
- Perfect for Birthdays and Anniversaries
- Rentals available hourly, daily, and weekly
- Group Rentals available at discounted rates
- Enter to win a free rental - url and QR code

Industry/Entity Type

Car Rental

Font styles to use
Serif
Sans Serif

Colors

Designer to choose colors to be used in the design.

Requirements
Must have
• FRONT:
• Please include our phone number and website:
• 832-519-2086
• www.BrazosTrikeHire.com
• BACK:
• REQUIREMENTS
• At least 25 years of age
• Valid Driver's License
• Debit or Credit Card
• Must know how to drive a manual transmission or stick shift

```html
<!DOCTYPE html>
<html lang="en">
<head>
<meta charset="utf-8">
<title>Brazos Trike Hire – Flyer Front and Back</title>
<link href="https://fonts.googleapis.com/css2?family=Arimo:wght@700&family=Roboto+Condensed:wght@600;700&display=swap" rel="stylesheet">
<style>
  :root{
    --red:#e8214f;
    --red-deep:#a50f2c;
    --ink:#111111;
    --charcoal:#2b2d30;
    --grey:#9ea3a6;
    --grey-light:#c9cdd0;
    --white:#ffffff;
    --page:#ffffff;
  }
  *{margin:0;padding:0;box-sizing:border-box}
  html,body{width:1200px;height:903px;overflow:hidden;background:var(--page)}
  .canvas{position:relative;width:1200px;height:903px}
  .card{position:absolute;top:10px;width:589px;height:883px;overflow:hidden;background:var(--white);border:1px solid #cfcfcf}
  .card--front{left:8px}
  .card--back{left:605px}
  .top-bar{position:absolute;left:0;top:0;width:100%;height:39px;background:var(--ink)}
  .bg{position:absolute;inset:0;width:100%;height:100%}

  /* front */
  .vehicle-art{position:absolute;border-radius:50% 46% 48% 44%}
  .vehicle-art--front{left:45px;top:80px;width:500px;height:390px;
    background:radial-gradient(ellipse at 50% 55%, #3a3c40 0%, #5b5f63 35%, #c7cbce 62%, rgba(255,255,255,0) 75%)}
  .brand-name{position:absolute;left:0;width:100%;top:540px;text-align:center;
    font-family:"Arimo",Arial,sans-serif;font-weight:700;font-size:40px;letter-spacing:2px;color:var(--charcoal)}
  .contact{position:absolute;left:0;width:100%;text-align:center;color:var(--white);
    font-family:"Roboto Condensed","Arial Narrow",sans-serif;font-weight:700}
  .contact--phone{top:730px;font-size:54px;letter-spacing:.5px}
  .contact--web{top:795px;font-size:25px}

  /* back */
  .ribbon{position:absolute;left:-50px;top:78px;width:400px;height:40px;background:var(--ink);
    transform:rotate(-29deg);transform-origin:50% 50%;color:var(--white);
    font-family:"Arimo",Arial,sans-serif;font-weight:700;font-size:24px;letter-spacing:.5px;
    display:flex;align-items:center;justify-content:center;padding-left:20px}
  .req-list{position:absolute;left:82px;top:130px;list-style:none;color:var(--white);
    font-family:"Arimo",Arial,sans-serif;font-weight:700;font-size:30px;line-height:46px}
  .req-list li{position:relative;padding-left:46px}
  .req-list li::before{content:"\2192";position:absolute;left:0;top:-1px;font-size:28px;font-weight:700}
  .req-list .age{font-size:60px;color:var(--grey-light);vertical-align:-6px;line-height:40px}
  .perks{position:absolute;left:64px;top:444px;width:466px;height:218px;background:var(--ink);border-radius:14px}
  .perks__tab{position:absolute;left:82px;top:429px;width:217px;height:32px;background:var(--grey);
    color:var(--white);font-family:"Arimo",Arial,sans-serif;font-weight:700;font-size:21px;
    display:flex;align-items:center;justify-content:center;border-radius:3px}
  .perks__list{position:absolute;left:96px;top:477px;list-style:none;color:var(--white);
    font-family:"Roboto Condensed","Arial Narrow",sans-serif;font-weight:700;font-size:22px;line-height:41.5px}
  .perks__list li{position:relative;padding-left:22px}
  .perks__list li::before{content:"";position:absolute;left:-4px;top:14px;width:13px;height:13px;border-radius:50%;background:var(--red)}
  .vehicle-art--back{left:150px;top:660px;width:460px;height:240px;
    background:radial-gradient(ellipse at 50% 55%, #3a3c40 0%, #5b5f63 40%, #c7cbce 65%, rgba(255,255,255,0) 78%)}
  .code-box{position:absolute;left:48px;top:771px;width:169px;height:83px;background:var(--ink);
    border:1px solid var(--white);color:var(--white);display:flex;align-items:center;justify-content:center;
    font-family:"Arimo",Arial,sans-serif;font-weight:700;font-size:20px}
  .back-web{position:absolute;left:238px;top:800px;color:var(--white);
    font-family:"Roboto Condensed","Arial Narrow",sans-serif;font-weight:700;font-size:23px}
</style>
</head>
<body>
<div class="canvas">

  <section class="card card--front">
    <div class="top-bar"></div>
    <div class="vehicle-art vehicle-art--front" role="img" aria-label="Illustration of a red and black three-wheeled roadster over grey brush strokes"></div>
    <div class="brand-name">BRAZOS TRIKE HIRE</div>
    <svg class="bg" viewBox="0 0 589 883" aria-hidden="true">
      <defs>
        <linearGradient id="frontBand" x1="0" y1="0" x2="0" y2="1">
          <stop offset="0" stop-color="var(--red-deep)"/>
          <stop offset=".35" stop-color="var(--red)"/>
          <stop offset="1" stop-color="var(--red)"/>
        </linearGradient>
      </defs>
      <path d="M0 685 H272 L294 707 L316 685 H589 V883 H0 Z" fill="url(#frontBand)"/>
      <path d="M589 725 V770 L230 883 H110 Z" fill="var(--grey)"/>
      <path d="M589 805 V830 L420 883 H340 Z" fill="var(--grey-light)"/>
    </svg>
    <div class="contact contact--phone">832-519-2086</div>
    <div class="contact contact--web">www.BrazosTrikeHire.com</div>
  </section>

  <section class="card card--back">
    <svg class="bg" viewBox="0 0 589 883" aria-hidden="true">
      <defs>
        <linearGradient id="backBg" x1="0" y1="0" x2="0" y2="1">
          <stop offset="0" stop-color="var(--red-deep)"/>
          <stop offset=".3" stop-color="var(--red)"/>
          <stop offset=".44" stop-color="var(--red)"/>
          <stop offset=".56" stop-color="var(--white)"/>
        </linearGradient>
      </defs>
      <rect width="589" height="883" fill="url(#backBg)"/>
      <path d="M589 318 V365 L0 640 V590 Z" fill="var(--grey)"/>
      <path d="M589 370 V390 L300 530 H260 Z" fill="var(--grey-light)"/>
    </svg>
    <div class="top-bar"></div>
    <div class="ribbon">REQUIREMENTS</div>
    <ul class="req-list">
      <li>At least <span class="age">25</span> years of age</li>
      <li>Valid Driver's License</li>
      <li>Debit or Credit Card</li>
      <li>Must know how to drive a<br>manual transmission or<br>stick shift</li>
    </ul>
    <div class="perks"></div>
    <div class="perks__tab">REQUIREMENTS</div>
    <ul class="perks__list">
      <li>Perfect for Birthdays and Anniversaries</li>
      <li>Rentals available hourly, daily, and weekly</li>
      <li>Group Rentals available at discounted rates</li>
      <li>Enter to win a free rental</li>
    </ul>
    <div class="vehicle-art vehicle-art--back" role="img" aria-label="Illustration of a red and black three-wheeled roadster"></div>
    <div class="code-box">barcode</div>
    <div class="back-web">www.BrazosTrikeHire.com</div>
  </section>

</div>
</body>
</html>
```